Information Technology Company needs a Website...

We need a single page website for new technology company called:

MERIDEL FALLS TECHNOLOGY GROUP
Based in Ojai CA.

We are offering three primary services:

- Business Solutions

- IT Services

- Software Implementation and Consulting

We want a single page design where all content scrolls down/up on one page. We're looking for the following characteristics:

- Home/Landing
- Active background with panoramic view (Will provide content)

- Business Solutions, IT Services, Software Implementation and Consulting

List of software vendors we recommend (Company logos)

- About
- History
- Our Team
- Partners

I'll upload our new logo as soon as we get the design files. I'll also send over some example website layout's that we like shortly.

Target Market(s)

Small/Medium Businesses

Industry/Entity Type

Information Technology

Number of Pages Required

1 page

Font styles to use
Other font styles liked:
• Sansation

Requirements
Must have
• Full page browser width, easy navigation and visibility. Creative design, not like every other "Technology" website template. Should be the "One Page" design where each section is below the next and the user scrolls down the page through the whole site. I like the concept of the following website in the main "Whiteboard" image:
• http://www.plavorix.com/design/4829137
• And the way this site does the active panoramic background:
• http://www.kelbrantworks.com/
• Something interesting and appealing to potential clients looking for Small/Medium business solutions and IT Services.
• Use uploaded Logo to establish color and theme for website.
Should not have
• Look the same as every other information technology website template.

```html
<!DOCTYPE html>
<html lang="en">
<head>
<meta charset="utf-8">
<title>Meridel Falls Technology Group</title>
<link rel="stylesheet" href="https://fonts.googleapis.com/css2?family=Open+Sans:wght@400;600&family=Raleway:wght@400;500&display=swap">
<style>
:root{
  --orange:#f15a24;
  --dark:#222222;
  --ink:#333333;
  --muted:#666666;
  --soft:#f5f5f5;
  --line:#e3e3e3;
  --white:#ffffff;
}
*{margin:0;padding:0;box-sizing:border-box}
html,body{width:1200px;height:2161px;overflow:hidden}
body{position:relative;background:var(--white);font-family:"Open Sans",sans-serif;color:var(--ink)}
.abs{position:absolute}

/* header */
.site-header{position:absolute;top:0;left:0;width:1200px;height:54px;background:var(--white);z-index:3}
.brand{position:absolute;left:89px;top:12px;display:flex;align-items:center;gap:8px}
.brand-mark{width:12px;height:12px;background:var(--orange);border-radius:50%}
.brand-name{font-family:"Raleway",sans-serif;font-weight:500;font-size:17px;color:var(--ink);line-height:1.1}
.brand-name small{display:block;font-size:7px;letter-spacing:1.4px}
.main-nav{position:absolute;right:91px;top:0;display:flex;height:54px}
.main-nav a{display:block;padding:0 12px;line-height:58px;font-size:11px;color:var(--ink);text-decoration:none;letter-spacing:.2px}
.main-nav a.active{color:var(--orange);border-bottom:2px solid var(--orange);line-height:56px}

/* hero */
.hero{position:absolute;top:54px;left:0;width:1200px;height:630px}
.hero-photo{position:absolute;inset:0}
.hero-title{position:absolute;right:91px;top:152px;text-align:right;color:var(--white);font-family:"Raleway",sans-serif}
.hero-title .lead{font-size:32px;line-height:38px}
.hero-title .lead span{color:var(--orange)}
.hero-title .big{font-size:49px;line-height:56px}
.hero-text{position:absolute;right:91px;top:266px;width:460px;text-align:right;color:var(--white);font-size:11.5px;line-height:21px}
.section-dots{position:absolute;left:16px;top:118px}
.section-dots i{display:block;width:9px;height:9px;border:1px solid #ddd;border-radius:50%;margin-bottom:6px}
.section-dots .current{position:relative}
.section-dots .current::after{content:"";position:absolute;left:3px;top:3px;width:3px;height:3px;background:#fff;border-radius:50%}
.section-dots span{position:absolute;left:13px;top:-4px;color:#fff;font-size:10px;white-space:nowrap}
.section-dots span::before{content:"";display:inline-block;width:12px;height:1px;background:#fff;vertical-align:middle;margin-right:5px}
.slide-arrow{position:absolute;top:400px;width:32px;height:32px;border-radius:50%;border:1.5px solid var(--white)}
.slide-arrow.next{border-color:var(--orange)}

/* about */
.about-visual{position:absolute;left:90px;top:544px;width:362px;height:372px}
.about-copy{position:absolute;left:488px;top:632px;width:620px}
.section-heading{font-family:"Raleway",sans-serif;font-weight:400;color:var(--orange);font-size:32px;line-height:36px}
.about-copy h3{font-family:"Raleway",sans-serif;font-weight:400;font-size:20px;margin-top:4px;color:var(--ink)}
.about-copy p{font-size:11.4px;line-height:19.5px;color:var(--muted);margin-top:12px}
.about-copy p + p{margin-top:5px}
.btn{display:inline-block;margin-top:25px;background:var(--orange);color:var(--white);font-size:10.5px;border-radius:20px;width:110px;height:39px;line-height:39px;text-align:center}

/* services */
.services{position:absolute;top:975px;left:0;width:1200px;height:352px;background:var(--soft)}
.centered-title{position:absolute;left:0;width:1200px;text-align:center;font-size:24px}
.service{position:absolute;top:95px;width:300px;text-align:center}
.service-icon{width:112px;height:112px;margin:0 auto}
.service h3{font-family:"Open Sans",sans-serif;font-weight:400;font-size:16.5px;margin-top:22px;color:var(--ink)}
.service p{font-size:11.4px;line-height:19.5px;color:var(--muted);margin-top:8px}

/* team */
.team-card{position:absolute;top:1413px;width:233px;height:257px;border:1px solid var(--line);background:var(--white)}
.team-photo{height:200px}
.team-plus{position:absolute;left:100px;top:184px;width:32px;height:32px;border-radius:50%;background:var(--orange)}
.team-plus::before,.team-plus::after{content:"";position:absolute;background:#fff;left:15px;top:9px;width:2px;height:14px}
.team-plus::after{transform:rotate(90deg)}
.team-name{position:absolute;top:225px;width:100%;text-align:center;font-size:11.5px;color:#888;text-transform:uppercase}

/* partners */
.partners{position:absolute;top:1719px;left:0;width:1200px;height:206px;background:var(--soft)}
.partner-box{position:absolute;top:82px;width:180px;height:77px;background:var(--white);border:1px solid var(--line);display:flex;align-items:center;justify-content:center}
.partner-badge{width:90px;height:26px;border-radius:3px;background:#c9c9c9}
.partner-badge.accent{background:var(--orange)}

/* footer */
.site-footer{position:absolute;top:1925px;left:0;width:1200px;height:236px;background:var(--dark);overflow:hidden}
.footer-col{position:absolute;top:34px;color:var(--white)}
.footer-col h4{font-family:"Raleway",sans-serif;font-weight:500;font-size:15.5px;margin-bottom:10px}
.footer-col p,.footer-col li{font-size:10.8px;line-height:19.5px}
.footer-col ul{list-style:none}
.newsletter{margin-top:10px;width:213px;border-bottom:1px solid #777;height:30px;position:relative;font-size:10.5px;color:#aaa;line-height:30px;padding-left:8px}
.contact-row{display:flex;gap:12px;align-items:flex-start;margin-bottom:6px}
.contact-row svg{flex:none;margin-top:5px}
.footer-corner{position:absolute;right:0;bottom:40px}
.footer-bar{position:absolute;left:0;bottom:0;width:1200px;height:40px;background:var(--orange);color:var(--white);font-size:11px;line-height:40px;padding-left:89px}
.social{position:absolute;right:85px;top:13px;display:flex;gap:19px}
.social i{display:block;width:13px;height:13px;border-radius:50%;background:var(--white)}
</style>
</head>
<body>

<header class="site-header">
  <div class="brand">
    <span class="brand-mark"></span>
    <span class="brand-name">meridel falls<small>TECHNOLOGY GROUP</small></span>
  </div>
  <nav class="main-nav">
    <a class="active">HOME</a><a>ABOUT</a><a>SOLUTIONS</a><a>OUR TEAM</a><a>PARTNERS</a><a>CONTACT</a>
  </nav>
</header>

<section class="hero">
  <svg class="hero-photo" width="1200" height="630" viewBox="0 0 1200 630">
    <defs>
      <linearGradient id="heroShade" x1="0" y1="0" x2="1" y2="1">
        <stop offset="0" stop-color="#4a4a4a"/>
        <stop offset=".45" stop-color="#2e3035"/>
        <stop offset="1" stop-color="#141516"/>
      </linearGradient>
    </defs>
    <rect width="1200" height="630" fill="url(#heroShade)" role="img" aria-label="Panoramic photo of a person working on a tablet at a desk"/>
    <polygon points="0,285 1004,610 1200,508 1200,630 0,630" fill="var(--orange)"/>
    <polygon points="0,316 1004,623 1200,545 1200,630 0,630" fill="var(--white)"/>
  </svg>
  <div class="section-dots">
    <i class="current"><span>HOME</span></i><i></i><i></i><i></i><i></i><i></i>
  </div>
  <div class="hero-title">
    <div class="lead">WELCOME TO <span>MERIDEL FALLS</span></div>
    <div class="big">TECHNOLOGY GROUP</div>
  </div>
  <p class="hero-text">Lorem Ipsum is simply dummy text of the printing and typesetting industry. Lorem Ipsum has been the industry's standard dummy text ever since the 1500s.</p>
  <svg class="slide-arrow" style="left:1036px" viewBox="0 0 32 32"><path d="M18 11l-5 5 5 5" stroke="#fff" stroke-width="1.6" fill="none"/></svg>
  <svg class="slide-arrow next" style="left:1076px" viewBox="0 0 32 32"><path d="M14 11l5 5-5 5" stroke="#f15a24" stroke-width="1.6" fill="none"/></svg>
</section>

<section class="about">
  <svg class="about-visual" viewBox="0 0 362 372">
    <defs>
      <linearGradient id="deskA" x1="0" y1="0" x2="1" y2="1"><stop offset="0" stop-color="#d8a56a"/><stop offset="1" stop-color="#4d4d52"/></linearGradient>
      <linearGradient id="deskB" x1="0" y1="0" x2="1" y2="1"><stop offset="0" stop-color="#eef1f4"/><stop offset="1" stop-color="#8a9aa8"/></linearGradient>
      <linearGradient id="deskC" x1="0" y1="0" x2="1" y2="1"><stop offset="0" stop-color="#f3efe9"/><stop offset="1" stop-color="#b58b6c"/></linearGradient>
      <linearGradient id="deskD" x1="0" y1="0" x2="1" y2="1"><stop offset="0" stop-color="#e9e4df"/><stop offset="1" stop-color="#7fa8c9"/></linearGradient>
    </defs>
    <g role="img" aria-label="Collage of office photos: laptops, charts and hands at work">
      <polygon points="181,0 271,90 181,180 91,90" fill="url(#deskA)"/>
      <polygon points="91,96 178,183 91,270 4,183" fill="url(#deskB)"/>
      <polygon points="274,96 358,180 274,264 190,180" fill="url(#deskC)"/>
      <polygon points="181,192 272,280 181,372 90,280" fill="url(#deskD)"/>
    </g>
  </svg>
  <div class="about-copy">
    <h2 class="section-heading">ABOUT US</h2>
    <h3>Our History</h3>
    <p>Lorem Ipsum is simply dummy text of the printing and typesetting industry. Lorem Ipsum has been the industry's standard dummy text ever since the 1500s, when an unknown printer took a galley of type and scrambled it to make a type specimen book. It has survived not only five centuries.</p>
    <p>Lorem Ipsum is simply dummy text of the printing and typesetting industry. Lorem Ipsum has been the industry's standard dummy text ever since the 1500s, when an unknown printer took a galley of type and scrambled it to make a type specimen book. It has survived not only five centuries.</p>
    <span class="btn">READ MORE</span>
  </div>
</section>

<section class="services">
  <h2 class="section-heading centered-title" style="top:58px">OUR SERVICES</h2>
  <div class="service" style="left:86px">
    <svg class="service-icon" viewBox="0 0 112 112">
      <polygon points="56,0 112,56 56,112 0,56" fill="#333"/>
      <g fill="#fff"><circle cx="46" cy="45" r="5"/><circle cx="66" cy="45" r="5"/><rect x="40" y="52" width="12" height="16" rx="3"/><rect x="60" y="52" width="12" height="16" rx="3"/><circle cx="56" cy="56" r="3.5"/></g>
    </svg>
    <h3>Business Solutions</h3>
    <p>Lorem Ipsum is simply dummy text of the printing and typesetting industry. Lorem Ipsum has been the industry's standard dummy.</p>
  </div>
  <div class="service" style="left:446px">
    <svg class="service-icon" viewBox="0 0 112 112">
      <polygon points="56,0 112,56 56,112 0,56" fill="var(--orange)"/>
      <g fill="#fff"><path d="M40 56a8 8 0 0 1 6-11 11 11 0 0 1 21 2 7 7 0 0 1 5 9z"/><rect x="46" y="59" width="20" height="5"/><rect x="46" y="66" width="20" height="5"/></g>
    </svg>
    <h3>IT Services</h3>
    <p>Lorem Ipsum is simply dummy text of the printing and typesetting industry. Lorem Ipsum has been the industry's standard dummy.</p>
  </div>
  <div class="service" style="left:817px">
    <svg class="service-icon" viewBox="0 0 112 112">
      <polygon points="56,0 112,56 56,112 0,56" fill="#333"/>
      <g fill="#fff"><circle cx="51" cy="48" r="7"/><path d="M38 70a13 11 0 0 1 26 0z"/><circle cx="67" cy="44" r="5" fill="none" stroke="#fff" stroke-width="2.5"/></g>
    </svg>
    <h3>Soft Implementation and Consult</h3>
    <p>Lorem Ipsum is simply dummy text of the printing and typesetting industry. Lorem Ipsum has been the industry's standard dummy.</p>
  </div>
</section>

<section class="team">
  <h2 class="section-heading centered-title" style="top:1362px">OUR TEAM</h2>
  <div class="team-card" style="left:89px">
    <div class="team-photo" role="img" aria-label="Portrait of Dana Whitfield" style="background:linear-gradient(160deg,#dfe7ee,#c9a58c)"></div>
    <span class="team-plus"></span><div class="team-name">Dana Whitfield</div>
  </div>
  <div class="team-card" style="left:351px">
    <div class="team-photo" role="img" aria-label="Portrait of Owen Castellan" style="background:linear-gradient(160deg,#eef2f6,#9fb8d8)"></div>
    <span class="team-plus"></span><div class="team-name">Owen Castellan</div>
  </div>
  <div class="team-card" style="left:614px">
    <div class="team-photo" role="img" aria-label="Portrait of Priya Lindqvist" style="background:linear-gradient(160deg,#f4f4f4,#a9a29a)"></div>
    <span class="team-plus"></span><div class="team-name">Priya Lindqvist</div>
  </div>
  <div class="team-card" style="left:872px">
    <div class="team-photo" role="img" aria-label="Portrait of Marcus Adebayo" style="background:linear-gradient(160deg,#f2f2f2,#6a5446)"></div>
    <span class="team-plus"></span><div class="team-name">Marcus Adebayo</div>
  </div>
</section>

<section class="partners">
  <h2 class="section-heading centered-title" style="top:28px">PARTNERS</h2>
  <div class="partner-box" style="left:91px"><span class="partner-badge"></span></div>
  <div class="partner-box" style="left:301px"><span class="partner-badge accent"></span></div>
  <div class="partner-box" style="left:510px"><span class="partner-badge"></span></div>
  <div class="partner-box" style="left:720px"><span class="partner-badge"></span></div>
  <div class="partner-box" style="left:929px"><span class="partner-badge"></span></div>
</section>

<footer class="site-footer">
  <div class="footer-col" style="left:95px;width:245px">
    <h4>About</h4>
    <p>Aenean vulputate eleifend tellus aenean leo ligula porttitor eu consequat vitae eleifend ac enim aliquam lorem ante dapibus in viverra quis feugiat a tellus phasellus viverra nulla ut metus varius.</p>
  </div>
  <div class="footer-col" style="left:429px">
    <h4>Useful Links</h4>
    <ul><li>Home</li><li>About</li><li>Solutions</li><li>Our Team</li><li>Partners</li><li>Contact</li></ul>
  </div>
  <div class="footer-col" style="left:599px;width:230px">
    <h4>Follow Us</h4>
    <p>Subscribe to our newsletter to get latest updates and offers.</p>
    <div class="newsletter">Enter email
      <svg class="abs" style="right:8px;top:10px" width="12" height="12" viewBox="0 0 12 12"><path d="M0 5L12 0 8 12 6 7z" fill="#f15a24"/></svg>
    </div>
  </div>
  <div class="footer-col" style="left:880px;width:230px">
    <h4>Contact information</h4>
    <div class="contact-row"><svg width="8" height="11" viewBox="0 0 8 11"><path d="M4 0a4 4 0 0 1 4 4c0 3-4 7-4 7S0 7 0 4a4 4 0 0 1 4-4z" fill="#999"/></svg><p>Some address line here..., area info, City name, Country name.</p></div>
    <div class="contact-row"><svg width="9" height="9" viewBox="0 0 9 9"><path d="M1 0h2l1 2-1 1a5 5 0 0 0 3 3l1-1 2 1v2c-5 1-9-3-8-8z" fill="#999"/></svg><p>123 456 7890</p></div>
    <div class="contact-row"><svg width="10" height="8" viewBox="0 0 10 8"><rect width="10" height="8" fill="#999"/><path d="M0 0l5 4 5-4" stroke="#222" fill="none"/></svg><p>info@meridelfalls.com</p></div>
  </div>
  <svg class="footer-corner" width="76" height="83" viewBox="0 0 76 83"><polygon points="76,0 76,83 0,83" fill="var(--orange)"/></svg>
  <div class="footer-bar">© Meridel Falls Technology Group 2016. All Right Reserved.
    <div class="social"><i></i><i></i><i></i><i></i></div>
  </div>
</footer>

</body>
</html>
```